BRIM Outreach Partners Business Card Rebrand

Hello Designers! We are looking for help designing our new business card to go in conjunction with our company rebrand. Unfortunately, we have an event mid June that requires we get these printed ASAP (before our new website is launched.) We have a mostly complete Brand Book which I have uploaded to this request for your reference to company information, style, fonts. I've also enclosed our logo file in .eps & .jpg. Attached is a sample business card my boss liked but said was "too simple." I made it in Canva and do not profess to be a designer. NOT FOR DESIGN REFERENCE, ONLY FOR CONTEXT Here is what our old website looks like: https://brimoutreachpartners.com/.

```html
<!DOCTYPE html>
<html lang="en">
<head>
<meta charset="utf-8">
<title>BRIM Outreach Partners – Business Card</title>
<link rel="stylesheet" href="https://fonts.googleapis.com/css2?family=Montserrat:wght@800&family=Poppins:wght@300;400;600;700&display=swap">
<style>
  :root {
    --brand-blue: #45a9dc;
    --brand-black: #0b0b0b;
    --card-white: #ffffff;
    --card-shade: #e4e4e4;
    --text-grey: #4a4a4a;
    --backdrop: #d9dadc;
  }
  * { box-sizing: border-box; margin: 0; padding: 0; }
  html, body {
    width: 1200px; height: 900px; overflow: hidden;
    background: var(--backdrop);
    font-family: "Poppins", sans-serif;
  }
  .canvas { position: relative; width: 1200px; height: 900px; }

  .card {
    position: absolute; left: 250px; width: 700px; height: 400px;
    background: linear-gradient(100deg, var(--card-shade) 0%, var(--card-white) 65%);
    overflow: hidden;
    box-shadow: 0 10px 28px rgba(0,0,0,0.22);
  }
  .card--front { top: 35px; }
  .card--back { top: 465px; }

  .card__bands { position: absolute; left: 0; bottom: 0; width: 700px; height: 80px; }

  .brand {
    position: absolute; display: flex; align-items: center; gap: 14px;
  }
  .brand__dot {
    width: 58px; height: 58px; border-radius: 50%; background: var(--brand-blue); flex: none;
  }
  .brand__name {
    font-family: "Poppins", sans-serif; font-weight: 700; font-size: 27px;
    line-height: 1.05; color: var(--brand-black); width: 190px;
  }
  .card--front .brand { right: 36px; bottom: 96px; }
  .card--back .brand { right: 40px; top: 40px; }

  .web-address {
    position: absolute; left: 40px; top: 46px;
    font-family: "Poppins", sans-serif; font-weight: 600; font-size: 17px;
    letter-spacing: 0.42em; color: var(--brand-black);
  }
  .web-address__domain { color: var(--brand-blue); }

  .contact { position: absolute; left: 70px; top: 150px; color: var(--text-grey); }
  .contact__name {
    font-family: "Montserrat", sans-serif; font-weight: 800; font-size: 23px;
    color: var(--brand-black); letter-spacing: 0.01em;
  }
  .contact__role { font-weight: 300; font-size: 18px; margin-top: -2px; }
  .contact__location { font-weight: 300; font-size: 18px; line-height: 1.2; margin: 20px 0 0 44px; }
  .contact__list { list-style: none; margin: 16px 0 0 44px; }
  .contact__item {
    display: flex; align-items: center; gap: 10px;
    font-weight: 300; font-size: 17px; line-height: 1.45;
  }
  .contact__icon { width: 16px; height: 16px; flex: none; }
</style>
</head>
<body>
<main class="canvas">

  <section class="card card--front" aria-label="Business card front">
    <p class="web-address">www.<span class="web-address__domain">brimoutreachpartners</span>.com</p>
    <div class="brand">
      <span class="brand__dot"></span>
      <span class="brand__name">BRIM Outreach Partners</span>
    </div>
    <svg class="card__bands" viewBox="0 0 700 80" aria-hidden="true">
      <path d="M300 80 L320 58 L700 58 L700 80 Z" fill="var(--brand-black)"/>
      <path d="M0 80 L0 46 L305 46 Q322 46 332 56 L356 80 Z" fill="var(--brand-blue)"/>
    </svg>
  </section>

  <section class="card card--back" aria-label="Business card back">
    <div class="brand">
      <span class="brand__dot"></span>
      <span class="brand__name">BRIM Outreach Partners</span>
    </div>

    <div class="contact">
      <h1 class="contact__name">DANIEL MORROW-LANE</h1>
      <p class="contact__role">Managing Partner</p>
      <p class="contact__location">Portland, OR based<br>( Pacific Time )</p>
      <ul class="contact__list">
        <li class="contact__item">
          <svg class="contact__icon" viewBox="0 0 16 16" aria-hidden="true"><path d="M3 1.5 L6 4.5 L4.6 6.4 Q6 9.6 9.6 11.4 L11.5 10 L14.5 13 L12.8 14.7 Q6.5 14.6 1.3 3.2 Z" fill="var(--brand-blue)"/></svg>
          +503-555-0142
        </li>
        <li class="contact__item">
          <svg class="contact__icon" viewBox="0 0 16 16" aria-hidden="true"><rect x="1" y="3" width="14" height="10" fill="var(--brand-blue)"/><path d="M1 3 L8 9 L15 3" fill="none" stroke="#fff" stroke-width="1.3"/></svg>
          daniel@brimoutreachpartners.com
        </li>
        <li class="contact__item">
          <svg class="contact__icon" viewBox="0 0 16 16" aria-hidden="true"><g fill="none" stroke="var(--brand-blue)" stroke-width="1.2"><circle cx="8" cy="8" r="6.5"/><ellipse cx="8" cy="8" rx="3" ry="6.5"/><path d="M1.5 8 H14.5 M2.6 4.6 H13.4 M2.6 11.4 H13.4"/></g></svg>
          www.brimoutreachpartners.com
        </li>
      </ul>
    </div>

    <svg class="card__bands" viewBox="0 0 700 80" aria-hidden="true">
      <path d="M0 80 L0 58 L500 58 L490 80 Z" fill="var(--brand-black)"/>
      <path d="M485 80 L485 44 Q485 24 505 24 L700 24 L700 80 Z" fill="var(--brand-blue)"/>
    </svg>
  </section>

</main>
</body>
</html>
```